Promotion for Local Garage - Harlow Motorworks offering 10% off

We are after an A5 Colour Leaflet to promote our business Harlow Motorworks.

Harlow Motorworks is a local garage and we are about to launch a flyer campaign in the local area.

Services we provide:
Servicing, Repairs, Diagnostics, Clutches, Brakes, Exhaust for all makes and models of cars and vans.

10% discount for anyone who brings in this flyer with them.

Company contact details below:
Telephone 0151 3846172
Website www.harlowmotorworks-example.co.uk

Address
Unit 4 Hollin Workshops,
Brackwell Lane,
Fenwick Ind Estate,
Ellesmere Port,
CH64 9QP

Our Logo is attached

Target Market(s)

Local Residents and businesses

Industry/Entity Type

Auto Repair

Requirements
Must have
• Services we provide:
• Servicing, Repairs, Diagnostics, Clutches, Brakes, Exhaust for all makes and models of cars and vans.
• 10% discount for anyone who brings in this flyer with them.
• Company contact details below:
• Telephone 0151 3846172
• Website www.harlowmotorworks-example.co.uk
• Address
• Unit 4 Hollin Workshops,
• Brackwell Lane,
• Fenwick Ind Estate,
• Ellesmere Port,
• CH64 9QP

```html
<!DOCTYPE html>
<html lang="en">
<head>
<meta charset="utf-8">
<title>Harlow Motorworks – A5 Leaflet</title>
<link rel="stylesheet" href="https://fonts.googleapis.com/css2?family=Questrial&family=Montserrat:wght@700&display=swap">
<style>
  :root {
    --backdrop: #e8e3de;
    --paper: #ffffff;
    --slate: #5b5b5d;
    --red: #e3262d;
    --white: #ffffff;
    --logo-grey: #3a3a3c;
  }
  * { margin: 0; padding: 0; box-sizing: border-box; }
  html, body {
    width: 1200px; height: 1200px; overflow: hidden;
    background: var(--backdrop);
  }
  .leaflet {
    position: absolute; left: 220px; top: 62px;
    width: 760px; height: 1076px;
    background: var(--paper);
    overflow: hidden;
    box-shadow: 0 6px 24px rgba(0,0,0,.18);
    font-family: "Questrial", sans-serif;
    color: var(--white);
  }
  .leaflet__shapes { position: absolute; inset: 0; }
  .brand {
    position: absolute; right: 70px; top: 80px;
    display: flex; align-items: center; gap: 12px;
    font-size: 32px; color: var(--logo-grey);
    white-space: nowrap;
  }
  .brand__dot {
    width: 15px; height: 15px; border-radius: 50%;
    background: var(--red);
  }
  .services {
    position: absolute; left: 70px; top: 290px;
    font-size: 27px; line-height: 1.18;
  }
  .services__title { margin-bottom: 2px; }
  .services__list { list-style: none; padding-left: 8px; }
  .services__list li::before { content: "• "; }
  .band-name {
    position: absolute; right: 0; top: 520px;
    width: 300px; height: 62px;
    display: flex; align-items: center; justify-content: center;
    font-family: "Montserrat", sans-serif; font-weight: 700;
    font-size: 23px; white-space: nowrap;
  }
  .band-offer {
    position: absolute; right: 0; top: 648px;
    width: 400px; height: 32px;
    display: flex; align-items: center; justify-content: center;
    font-size: 11px; letter-spacing: .3px; text-transform: uppercase;
    white-space: nowrap;
  }
  .contact {
    position: absolute; right: 38px; top: 716px;
    text-align: right; font-size: 15px; line-height: 1.3;
    font-style: normal;
  }
  .contact__label { margin-bottom: 8px; }
  .contact__row { display: flex; justify-content: flex-end; align-items: flex-start; gap: 7px; }
  .contact__icon { width: 13px; height: 13px; margin-top: 3px; flex: none; }
  .website {
    position: absolute; left: 290px; right: 10px; top: 1000px;
    text-align: center; font-size: 13px; letter-spacing: 3.5px;
    white-space: nowrap;
  }
</style>
</head>
<body>
<main class="leaflet">
  <svg class="leaflet__shapes" width="760" height="1076" viewBox="0 0 760 1076">
    <defs>
      <linearGradient id="engineTone" x1="0" y1="0" x2="1" y2="1">
        <stop offset="0" stop-color="#1c1c1d"/>
        <stop offset="0.55" stop-color="#4a4a4c"/>
        <stop offset="1" stop-color="#777779"/>
      </linearGradient>
    </defs>
    <g role="img" aria-label="Close-up photograph of a car engine component">
      <polygon points="0,150 560,356 300,1076 0,1076" fill="url(#engineTone)"/>
    </g>
    <polygon class="slate-panel" points="560,356 760,430 760,1076 300,1076" fill="var(--slate)"/>
    <polygon class="band-name-shape" points="501,520 760,520 760,582 479,582" fill="var(--red)"/>
    <polygon class="band-offer-shape" points="360,648 760,648 760,680 360,680" fill="var(--red)"/>
  </svg>

  <div class="brand"><span>Harlow Motorworks</span><span class="brand__dot"></span></div>

  <div class="services">
    <p class="services__title">Services we provide:</p>
    <ul class="services__list">
      <li>Servicing</li>
      <li>Repairs</li>
      <li>Diagnostics</li>
      <li>Clutches</li>
      <li>Brakes</li>
      <li>Exhaust for all makes</li>
      <li>models of cars and vans</li>
    </ul>
  </div>

  <div class="band-name">Harlow Motorworks</div>
  <div class="band-offer">10% discount for anyone who brings in this flyer with them</div>

  <address class="contact">
    <div class="contact__label">Company contact :</div>
    <div class="contact__row"><span>0151 3846172</span>
      <svg class="contact__icon" viewBox="0 0 16 16"><circle cx="8" cy="8" r="8" fill="#fff"/><path d="M5 4.5l1.6-.4.9 2-1 .8a6 6 0 0 0 2.6 2.6l.8-1 2 .9-.4 1.6c-3.5.3-6.8-3-6.5-6.5z" fill="var(--slate)"/></svg>
    </div>
    <div class="contact__row"><span>Unit 4 Hollin Workshops,<br>Brackwell Lane,<br>Fenwick Ind Estate,<br>Ellesmere Port,<br>CH64 9QP</span>
      <svg class="contact__icon" viewBox="0 0 16 16"><circle cx="8" cy="8" r="8" fill="#fff"/><path d="M8 3.5a3 3 0 0 0-3 3c0 2.2 3 6 3 6s3-3.8 3-6a3 3 0 0 0-3-3zm0 4.2a1.2 1.2 0 1 1 0-2.4 1.2 1.2 0 0 1 0 2.4z" fill="var(--slate)"/></svg>
    </div>
  </address>

  <div class="website">www.harlowmotorworks-example.co.uk</div>
</main>
</body>
</html>
```